political campaign lawn sign - Governor's Council in Massachuesetts

We are looking for a political lawn sign. We are running a campaign for Governor's Council in Massachusetts. This sign will be on the lawn of homes and businesses so people driving by will see it. It needs to be simple and bold. The last name is long so maybe it could say vote for Marty and then Kolbeck will be big a bold on the next line??
We need it to say:
Vote for Martin Kolbeck
Governor's Council.

Target Market(s)

local residents

Industry/Entity Type

Politcal Campaign

Font styles to use
Sans Serif
Other font styles liked:
• not sure what font but a modern looking one such as Helvetica, Arial, Sans Seri, sharp sans..

Colors
0054AA
0677BA
7BADD7
CADEEF
E8F1F8
00AB8E
00BBA5
67D7C9
C6EFE9
E9F9F6
FFF300
FFF600
FEFA6F
FFFEC7
FFFEE8

Requirements
Must have
• My name written out with a Capital D and R but lower case for every other letter so its Marty Kolbeck
Nice to have
• modern font , the Colors of the lawn sign should have Blue, Yellow and White something bold that will stand out
Should not have
• any maps of Massachusetts

```html
<!DOCTYPE html>
<html lang="en">
<head>
<meta charset="UTF-8">
<title>Vote For Martin Kolbeck – Governor's Council</title>
<link href="https://fonts.googleapis.com/css2?family=Roboto:wght@700&family=Lato:wght@900&display=swap" rel="stylesheet">
<style>
  :root {
    --page-bg: #212121;
    --sign-blue: #0677BA;
    --stripe-blue: #0054AA;
    --sign-yellow: #FFF600;
    --text-white: #FFFFFF;
    --text-soft-white: #E8F1F8;
  }
  html, body {
    margin: 0;
    padding: 0;
    width: 1129px;
    height: 1200px;
    overflow: hidden;
    background: var(--page-bg);
  }
  .canvas {
    position: relative;
    width: 1129px;
    height: 1200px;
    display: flex;
    align-items: center;
    justify-content: center;
  }
  .lawn-sign {
    display: block;
    width: 1009px;
    height: 299px;
  }
  .sign-field { fill: var(--sign-blue); }
  .accent-stripe { fill: var(--stripe-blue); }
  .footer-band { fill: var(--sign-yellow); }
  .kicker {
    font-family: "Roboto", Arial, sans-serif;
    font-weight: 700;
    font-size: 86px;
    fill: var(--text-soft-white);
  }
  .candidate-name {
    font-family: "Roboto", Arial, sans-serif;
    font-weight: 700;
    font-size: 215px;
    fill: var(--text-white);
    filter: drop-shadow(7px 6px 0 var(--stripe-blue));
  }
  .office-name {
    font-family: "Lato", Arial, sans-serif;
    font-weight: 900;
    font-size: 108px;
    fill: var(--sign-blue);
  }
</style>
</head>
<body>
<main class="canvas">
  <svg class="lawn-sign" viewBox="0 0 1634 484" xmlns="http://www.w3.org/2000/svg" aria-label="Vote For Martin Kolbeck, Governor's Council">
    <rect class="sign-field" x="0" y="0" width="1634" height="484"/>
    <rect class="accent-stripe" x="0" y="52" width="604" height="25"/>
    <rect class="accent-stripe" x="1015" y="52" width="619" height="25"/>
    <text class="kicker" x="817" y="92" text-anchor="middle">Vote For</text>
    <text class="candidate-name" x="817" y="287" text-anchor="middle" textLength="1480" lengthAdjust="spacingAndGlyphs">Martin Kolbeck</text>
    <path class="footer-band" d="M0 402 H255 Q285 402 288 372 Q292 337 325 337 H1300 Q1340 337 1345 372 Q1350 402 1380 402 H1634 V484 H0 Z"/>
    <text class="office-name" x="817" y="447" text-anchor="middle">Governor's Council.</text>
  </svg>
</main>
</body>
</html>
```